School Bumper Sticker for Parents Design

We need an updated/re-designed bumper sticker for parents to put on their cars. We are a private non-profit school in Maryland serving children aged 3-9. We would like the bumper sticker to still include the information that was on our previous bumper sticker (attached) - but in a more professional/attractive way. We want people to see the bumper sticker and get curious about Montessori education and our school!

Industry/Entity Type

Education

Colors

Designer to choose colors to be used in the design.

Requirements
Must have
• Name of school, city/state, website address, Some of the interesting info from the previous bumper sticker
Nice to have
• logo
Should not have
• no cartoons or very young child/daycare images

```html
<!DOCTYPE html>
<html lang="en">
<head>
<meta charset="utf-8">
<title>Maple Grove Montessori – Bumper Sticker</title>
<link rel="stylesheet" href="https://fonts.googleapis.com/css2?family=Poppins:ital,wght@0,400;0,700;0,800;1,300;1,400;1,700&display=swap">
<style>
  :root {
    --navy: #2f4b8a;
    --green: #1f9a55;
    --teal: #17958f;
    --pink: #f1a3a6;
    --purple: #9a5aa6;
    --orange: #f7941d;
    --blue: #1d7bb8;
    --paper: #ffffff;
    --stage: #eef0f2;
  }
  * { box-sizing: border-box; margin: 0; padding: 0; }
  html, body {
    width: 1200px; height: 675px; overflow: hidden;
    background: var(--stage);
    font-family: "Poppins", sans-serif;
  }
  .stage {
    width: 1200px; height: 675px;
    display: flex; align-items: center; justify-content: center;
  }
  .sticker {
    position: relative;
    width: 1050px; height: 380px;
    background: var(--paper);
    border: 4px solid var(--teal);
    border-right-color: var(--purple);
    border-top-color: var(--purple);
    box-shadow: 0 6px 20px rgba(0,0,0,.12);
  }
  .headline {
    position: absolute; left: 22px; top: 14px;
    color: var(--navy);
    font-weight: 800; font-size: 70px; line-height: 1;
    letter-spacing: -1px; white-space: nowrap;
  }
  .headline .child {
    color: var(--green); font-weight: 300; font-style: italic;
    font-size: 80px; letter-spacing: 0;
  }
  .headline .and { font-size: 40px; letter-spacing: 0; }
  .band {
    position: absolute; height: 44px;
    display: flex; align-items: center; justify-content: center;
    color: #fff; font-weight: 700; font-style: italic;
    font-size: 21px; text-transform: uppercase; white-space: nowrap;
  }
  .band--teal { left: 0; top: 112px; width: 470px; background: var(--teal); }
  .band--pink { left: 470px; top: 112px; width: 252px; background: var(--pink); font-weight: 400; }
  .band--purple { left: 722px; top: 100px; width: 320px; background: var(--purple); }
  .band--orange { left: 190px; top: 156px; width: 460px; background: var(--orange); }
  .band--blue { left: 650px; top: 144px; width: 392px; background: var(--blue); }
  .brand {
    position: absolute; left: 14px; top: 214px;
    width: 160px; text-align: center;
  }
  .brand__mark {
    display: block; width: 110px; height: 110px; margin: 0 auto 8px;
    background: var(--navy);
  }
  .brand__name {
    color: var(--navy); font-weight: 700; font-size: 20px;
    line-height: 1.1; text-transform: uppercase;
  }
  .question {
    position: absolute; left: 196px; top: 218px;
    color: var(--navy); font-weight: 800; font-size: 60px;
    line-height: 1; letter-spacing: -1px; white-space: nowrap;
  }
  .answer {
    position: absolute; right: 20px; top: 222px;
    color: var(--green); font-weight: 300; font-style: italic;
    font-size: 40px; line-height: 1;
  }
  .website {
    position: absolute; left: 200px; bottom: 22px;
    color: var(--purple); font-size: 26px; text-transform: uppercase;
  }
  .location {
    position: absolute; right: 22px; bottom: 62px;
    color: var(--purple); font-size: 20px; text-transform: uppercase;
  }
</style>
</head>
<body>
<main class="stage">
  <section class="sticker">
    <h1 class="headline">WHAT DOES MY <span class="child">CHILD</span> <span class="and">AND...</span></h1>

    <div class="band band--teal">The founder of Searchly.com</div>
    <div class="band band--pink">Edwin Harlow</div>
    <div class="band band--purple">Augustus Reed Marlow</div>
    <div class="band band--orange">The founder of OpenLore.org</div>
    <div class="band band--blue">The founder of ShopRiver.com</div>

    <div class="brand">
      <span class="brand__mark"></span>
      <p class="brand__name">Maple Grove</p>
    </div>

    <p class="question">HAVE IN COMMON?</p>
    <p class="answer">MONTESSORI.</p>
    <p class="website">www.maplegrovemontessori.org</p>
    <p class="location">Brookfield, MD</p>
  </section>
</main>
</body>
</html>
```